RW Frameworks Inc Business cards

We need business cards using our existing logo but slightly modified. Right now the logo says RW Framework Masonry. We want to keep the RW part of the design, but replace the Framework Masonry portion with "FRAMEWORKS". Please see the attached file.
Ideally this would be a blank template so we can add Different Names, titles, and phone numbers later.
On the one side we want only the logo and on the other side the detail. I'm attaching an example for you to see.
Please reach out with any other questions. Our address and other details will be given out once we find a design we like.

Target Market(s)

Construction Industry

```html
<!DOCTYPE html>
<html lang="en">
<head>
<meta charset="utf-8">
<title>RW Frameworks Inc Business Cards</title>
<link rel="stylesheet" href="https://fonts.googleapis.com/css2?family=Roboto:wght@400;500;700&family=Montserrat:wght@700&display=swap">
<style>
  :root {
    --bg: #e4e5e7;
    --brand-blue: #0a7ad4;
    --brand-blue-deep: #0568c0;
    --paper: #ffffff;
    --ink: #333333;
    --muted: #8a8a8a;
  }
  * { box-sizing: border-box; margin: 0; padding: 0; }
  html, body { width: 1200px; height: 800px; overflow: hidden; }
  body {
    background: var(--bg);
    font-family: "Roboto", Arial, sans-serif;
    display: flex;
    align-items: center;
    justify-content: center;
    gap: 60px;
  }
  .card {
    width: 504px;
    height: 288px;
    position: relative;
    box-shadow: 0 6px 18px rgba(0,0,0,0.12);
  }
  .card--front {
    background: linear-gradient(135deg, var(--brand-blue-deep), var(--brand-blue));
    display: flex;
    align-items: center;
    justify-content: center;
  }
  .card--back { background: var(--paper); }

  .wordmark {
    font-family: "Montserrat", Arial, sans-serif;
    font-weight: 700;
    letter-spacing: 0.08em;
    white-space: nowrap;
  }
  .card--front .wordmark {
    color: var(--paper);
    font-size: 40px;
  }
  .card--back .wordmark {
    position: absolute;
    right: 34px;
    top: 120px;
    color: var(--brand-blue);
    font-size: 19px;
  }

  .contact {
    position: absolute;
    left: 36px;
    top: 44px;
    color: var(--ink);
    font-size: 14px;
    line-height: 1.35;
  }
  .contact__name {
    color: var(--brand-blue);
    font-weight: 700;
    font-size: 19px;
    line-height: 1.2;
  }
  .contact__title { margin-bottom: 10px; }
  .contact__address { margin-bottom: 4px; }
  .contact__line {
    display: flex;
    align-items: center;
    gap: 6px;
  }
  .contact__icon { width: 12px; height: 12px; flex: none; }
</style>
</head>
<body>
  <section class="card card--front" aria-label="Card front">
    <span class="wordmark">RW FRAMEWORKS</span>
  </section>

  <section class="card card--back" aria-label="Card back">
    <div class="contact">
      <p class="contact__name">Dana Whitfield</p>
      <p class="contact__title">Director</p>
      <p class="contact__address">Ridgeline Road, Suite 210<br>Harbor Point, California</p>
      <p class="contact__line">
        <svg class="contact__icon" viewBox="0 0 12 12" aria-hidden="true"><path fill="var(--brand-blue)" d="M2.5 1h2l1 2.5-1.3 1a6 6 0 0 0 2.8 2.8l1-1.3L10.5 7v2a1.5 1.5 0 0 1-1.5 1.5A8.5 8.5 0 0 1 1 2.5 1.5 1.5 0 0 1 2.5 1z"/></svg>
        555.014.2290
      </p>
      <p class="contact__line">
        <svg class="contact__icon" viewBox="0 0 12 12" aria-hidden="true"><rect x="0.5" y="2" width="11" height="8" rx="1" fill="var(--brand-blue)"/><path d="M1 2.8 6 6.5l5-3.7" fill="none" stroke="#fff" stroke-width="1"/></svg>
        info@example.com
      </p>
      <p class="contact__line">
        <svg class="contact__icon" viewBox="0 0 12 12" aria-hidden="true"><circle cx="6" cy="6" r="5.5" fill="var(--brand-blue)"/><path d="M.5 6h11M6 .5c-2.5 3-2.5 8 0 11M6 .5c2.5 3 2.5 8 0 11" fill="none" stroke="#fff" stroke-width="0.8"/></svg>
        www.example.com
      </p>
    </div>
    <span class="wordmark">RW FRAMEWORKS</span>
  </section>
</body>
</html>
```